Wix Website design for my therapy business - Willowmere Group

I have started designing a Wix site and have a good idea of what I want.
I have set up the pages, created some design ideas, and inputted the copy. I need someone fabulous to finish off the design aspects. I like working closely with the designers, I was an interior designer in an old career.
I would like the site to be funky but professional. My Wix skills are limited, and I just can't achieve the look I am wanting without having to spend a lot of time learning. If it's easier to start over, that's ok providing you use the same colours, font, images etc. I have included a screenshot of the home page below. I have another site I need to start as soon as we have finished this one.
I am looking for someone who is a good listener and is has design flare. I am easy to get along with and will respond quickly.
I would like to set up SEO and have help in the future.
Let me know if you are the right person for the job.
Target Market(s)
Please needing help with their mental health and for therapy.
Industry/Entity Type
Mental health
Font styles to use
Other font styles liked:
- Futura light
Requirements
Must have
- be easy to navigate and be simple yet stylish
Nice to have
- I have set up the basics of the site - nice to haves are already on the site
Should not have
- old fashioned large chunks of text.

```html
<!DOCTYPE html>
<html lang="en">
<head>
<meta charset="utf-8">
<title>Willowmere Group – Massage Therapy</title>
<link href="https://fonts.googleapis.com/css2?family=Poppins:wght@300;400;500;600;700&display=swap" rel="stylesheet">
<style>
:root{
  --brown:#9f8262;
  --brown-dark:#8a6f52;
  --blue:#cfdde6;
  --ink:#333;
  --muted:#555;
  --soft:#f5f5f5;
  --slate:#555a64;
  --star:#f0901e;
}
*{box-sizing:border-box;margin:0;padding:0}
html,body{width:1200px;height:3988px;overflow:hidden}
body{font-family:'Poppins',sans-serif;color:var(--ink);background:#fff;position:relative}
.abs{position:absolute}
a{color:inherit;text-decoration:none}

/* header */
.site-header{position:absolute;left:0;top:0;width:1200px;height:132px;background:#fff}
.brand{position:absolute;left:85px;top:46px;display:flex;align-items:center;gap:10px;font-size:30px;font-weight:500;color:var(--brown);letter-spacing:.5px}
.brand-dot{width:14px;height:14px;border-radius:50%;background:var(--brown)}
.main-nav{position:absolute;right:85px;top:58px;display:flex;gap:28px;font-size:15px;color:var(--ink)}
.main-nav .active{color:var(--brown);position:relative}
.main-nav .active::after{content:"";position:absolute;left:-3px;right:-3px;top:34px;height:2px;background:var(--brown)}

/* hero */
.hero{position:absolute;left:0;top:132px;width:1200px;height:579px;background:linear-gradient(100deg,#e6e9ec 0%,#dcdfe2 40%,#cbb8a4 62%,#d9dadc 80%,#eef0f1 100%)}
.hero-kicker{position:absolute;left:85px;top:224px;font-size:20px;font-weight:300;color:var(--ink)}
.hero-title{position:absolute;left:85px;top:258px;font-size:42px;line-height:52px;font-weight:700;color:var(--brown)}
.hero-dots{position:absolute;left:551px;top:530px;display:flex;gap:8px}
.hero-dots span{width:12px;height:12px;border-radius:50%;background:rgba(255,255,255,.5)}
.hero-dots span:first-child{background:#fff}

/* section headings */
.kicker{font-size:19px;font-weight:300;color:var(--ink);text-transform:uppercase}
.title{font-weight:600;color:var(--brown)}
.center{position:absolute;left:0;width:1200px;text-align:center}

/* about */
.about-ring{position:absolute;left:277px;top:761px;width:180px;height:180px;border:23px solid var(--brown);border-radius:50%}
.about-photo-lg{position:absolute;left:82px;top:864px;width:356px;height:356px;border-radius:50%;border:10px solid var(--blue);background:linear-gradient(135deg,#efe6de,#c9a58c 55%,#e7dcd3)}
.about-photo-sm{position:absolute;left:280px;top:1087px;width:248px;height:248px;border-radius:50%;border:10px solid var(--brown);background:linear-gradient(135deg,#9fb2c3,#e8d3c2 50%,#d7c1ae)}
.about-dot{position:absolute;left:140px;top:1259px;width:80px;height:80px;border-radius:50%;background:var(--blue)}
.about-copy{position:absolute;left:599px;top:845px;width:506px}
.about-copy .title{font-size:41px;line-height:48px}
.about-copy p{margin-top:24px;font-size:15.5px;line-height:31px;font-weight:300;color:var(--muted);text-align:justify}
.btn-solid{display:inline-block;margin-top:38px;width:161px;height:52px;line-height:52px;text-align:center;background:var(--brown);color:#fff;font-size:14px;font-weight:500}

/* services */
.services{position:absolute;left:0;top:1355px;width:1200px;height:1000px;background:var(--soft)}
.service-card{position:absolute;width:491px;height:318px;background:#fff;box-shadow:0 2px 10px rgba(0,0,0,.12)}
.service-img{position:absolute;left:0;top:0;width:172px;height:135px}
.service-body{position:absolute;left:199px;top:48px;width:248px}
.service-body h3{font-size:30px;font-weight:300;color:var(--ink);line-height:38px}
.service-body p{margin-top:12px;font-size:15px;line-height:26px;font-weight:300;color:var(--muted);text-align:justify}
.service-body .more{display:block;margin-top:24px;font-size:14px;color:var(--brown);font-weight:500}

/* testimonials */
.quote-card{position:absolute;top:2596px;width:332px;height:240px;border:2px solid #ddd;border-top:3px solid var(--brown);border-radius:14px;background:#fff}
.quote-card p{position:absolute;left:30px;top:78px;width:272px;text-align:center;font-size:15px;line-height:26px;font-weight:300;color:var(--ink)}
.avatar{position:absolute;top:2558px;width:84px;height:84px;border-radius:50%;border:3px solid #fff;background:linear-gradient(160deg,#6b4a3a,#3d2b22)}
.client{position:absolute;top:2858px;width:332px;text-align:center}
.client strong{display:block;font-size:15px;font-weight:600}
.client span{display:block;font-size:14px;font-weight:300;color:var(--muted)}
.stars{display:flex;justify-content:center;gap:3px;margin-top:6px}
.arrow{position:absolute;top:2694px;width:54px;height:54px;border-radius:50%;background:var(--brown)}

/* blog */
.post{position:absolute;top:3178px;width:317px;height:250px}
.post-img{position:absolute;left:0;top:0;width:317px;height:200px}
.post-box{position:absolute;left:122px;top:99px;width:195px;height:146px;background:#fff;padding:16px 12px}
.post-box .date{font-size:11.5px;font-weight:300;color:var(--muted)}
.post-box h4{margin-top:8px;font-size:19px;font-weight:400;color:var(--brown)}
.post-box p{font-size:12px;line-height:17px;font-weight:400;color:var(--ink)}
.post-box .read{display:block;margin-top:13px;font-size:11px;font-style:italic;color:var(--brown)}
.btn-outline{position:absolute;left:531px;top:3483px;width:138px;height:53px;border:1px solid #777;line-height:51px;text-align:center;font-size:15px;color:var(--ink)}

/* footer */
.site-footer{position:absolute;left:0;top:3594px;width:1200px;height:335px;background:var(--brown);color:#fff}
.footer-brand{position:absolute;left:104px;top:104px;display:flex;align-items:center;gap:8px;font-size:22px;font-weight:500}
.footer-brand .brand-dot{background:#fff;width:11px;height:11px}
.footer-col{position:absolute;top:78px}
.footer-col h5{font-size:20px;font-weight:400;text-transform:uppercase}
.quick-links{list-style:none;margin-top:18px}
.quick-links li{font-size:15px;line-height:31px;position:relative;padding-left:16px}
.quick-links li::before{content:"";position:absolute;left:2px;top:14px;width:5px;height:5px;border-radius:50%;background:#fff}
.contact-row{display:flex;gap:12px;align-items:flex-start;font-size:15px;line-height:19px;margin-top:24px}
.contact-row svg{flex:none;margin-top:1px}
.newsletter p{margin-top:20px;font-size:15px;line-height:19px;width:250px}
.newsletter .field{margin-top:19px;width:249px;height:38px;background:#fff;border:1px solid #ddd}
.newsletter .subscribe{margin-top:13px;width:125px;height:36px;line-height:36px;text-align:center;background:var(--slate);font-size:13px;font-weight:500}
.copyright{position:absolute;left:0;top:3929px;width:1200px;height:59px;background:var(--slate);color:#fff;text-align:center;line-height:59px;font-size:15px}
</style>
</head>
<body>

<header class="site-header">
  <div class="brand"><span class="brand-dot"></span>Willowmere Group</div>
  <nav class="main-nav">
    <a class="active">Home</a><a>About Us</a><a>Services ▾</a><a>Program List</a><a>Resources</a><a>Blog</a><a>Contact Us</a>
  </nav>
</header>

<section class="hero" role="img" aria-label="Woman relaxing face down on a massage table while receiving a shoulder massage">
  <div class="hero-kicker">THE WILLOWMERE GROUP</div>
  <h1 class="hero-title">WELCOME TO OUR<br>MASSAGE THERAPY</h1>
  <div class="hero-dots"><span></span><span></span><span></span><span></span></div>
</section>

<section class="about">
  <div class="about-ring"></div>
  <div class="about-photo-lg" role="img" aria-label="Therapist giving a client a facial treatment"></div>
  <div class="about-photo-sm" role="img" aria-label="Client receiving a relaxing facial care session"></div>
  <div class="about-dot"></div>
  <div class="about-copy">
    <div class="kicker">Who we are</div>
    <h2 class="title">About Our Therapy</h2>
    <p>Lorem ipsum dolor sit amet, consectetur adipiscing elit, sed do eiusmod tempor incididunt ut labore et dolore magna aliqua. Ut enim ad minim veniam, quis nostrud exercitation ullamco laboris nisi ut aliquip ex ea commodo consequat. Duis aute irure dolor in reprehenderit in voluptate velit esse cillum dolore eu fugiat nulla pariatur. Excepteur sint occaecat cupidatat non proident, sunt in culpa qui officia .</p>
    <a class="btn-solid">LEARN MORE</a>
  </div>
</section>

<section class="services">
  <div class="center" style="top:92px"><div class="kicker">What we provide</div><h2 class="title" style="font-size:52px;line-height:60px;margin-top:-4px">Our Services</h2></div>

  <article class="service-card" style="left:87px;top:230px">
    <div class="service-img" role="img" aria-label="Therapist massaging a client's shoulders" style="background:linear-gradient(135deg,#e3d6c8,#6fb5a4 70%,#9ccfc2)"></div>
    <div class="service-body"><h3>EMDR</h3><p>Lorem ipsum dolor sit amet, consec tetur adipiscing elit. Etiam pellen tesque lacus ut elit malesuada dapibus. Morbi et Lorem ipsum dolor sit amet</p><a class="more">LEARN MORE</a></div>
  </article>
  <article class="service-card" style="left:622px;top:230px">
    <div class="service-img" role="img" aria-label="Hands massaging a client's neck" style="background:linear-gradient(135deg,#efe9e4,#d9b9a0 60%,#5a4234)"></div>
    <div class="service-body"><h3>Addictions</h3><p>Lorem ipsum dolor sit amet, consec tetur adipiscing elit. Etiam pellen tesque lacus ut elit malesuada dapibus. Morbi et Lorem ipsum dolor sit amet</p><a class="more">LEARN MORE</a></div>
  </article>
  <article class="service-card" style="left:87px;top:580px">
    <div class="service-img" role="img" aria-label="Hands giving a back massage" style="background:linear-gradient(135deg,#6d3a2a,#d59a80 55%,#8a4a36)"></div>
    <div class="service-body"><h3>Betrayal Trauma</h3><p>Lorem ipsum dolor sit amet, consec tetur adipiscing elit. Etiam pellen tesque lacus ut elit malesuada dapibus. Morbi et Lorem ipsum dolor sit amet</p><a class="more">LEARN MORE</a></div>
  </article>
  <article class="service-card" style="left:622px;top:580px">
    <div class="service-img" role="img" aria-label="Client receiving a head massage" style="background:linear-gradient(135deg,#7b3a2c,#c0504a 40%,#e2b59c)"></div>
    <div class="service-body"><h3>PTSD</h3><p>Lorem ipsum dolor sit amet, consec tetur adipiscing elit. Etiam pellen tesque lacus ut elit malesuada dapibus. Morbi et Lorem ipsum dolor sit amet</p><a class="more">LEARN MORE</a></div>
  </article>
</section>

<section class="testimonials">
  <div class="center" style="top:2442px"><div class="kicker">What our client says</div><h2 class="title" style="font-size:52px;line-height:60px;margin-top:-4px">Testimonials</h2></div>

  <div class="quote-card" style="left:85px"><p>Lorem ipsum dolor sit amet, con secte tur adipiscing elit. Pellen tesque aliquet eros vitae placerat Lorem ipsum dolor sit amet, con sectetur adipiscing elit</p></div>
  <div class="quote-card" style="left:434px"><p>Lorem ipsum dolor sit amet, con secte tur adipiscing elit. Pellen tesque aliquet eros vitae placerat Lorem ipsum dolor sit amet, con sectetur adipiscing elit</p></div>
  <div class="quote-card" style="left:782px"><p>Lorem ipsum dolor sit amet, con secte tur adipiscing elit. Pellen tesque aliquet eros vitae placerat Lorem ipsum dolor sit amet, con sectetur adipiscing elit</p></div>

  <div class="avatar" role="img" aria-label="Client portrait" style="left:209px"></div>
  <div class="avatar" role="img" aria-label="Client portrait" style="left:558px"></div>
  <div class="avatar" role="img" aria-label="Client portrait" style="left:906px"></div>

  <div class="client" style="left:85px"><strong>Lorem ipsum sit</strong><span>Lorem ipsum</span>
    <div class="stars"><svg width="102" height="18" viewBox="0 0 102 18"><g fill="var(--star)"><path id="st" d="M9 0l2.6 5.8 6.4.6-4.8 4.2 1.4 6.3L9 13.6 3.4 16.9l1.4-6.3L0 6.4l6.4-.6z"/><use href="#st" x="21"/><use href="#st" x="42"/><use href="#st" x="63"/><use href="#st" x="84"/></g></svg></div></div>
  <div class="client" style="left:434px"><strong>Lorem ipsum sit</strong><span>Lorem ipsum</span>
    <div class="stars"><svg width="102" height="18" viewBox="0 0 102 18"><g fill="var(--star)"><use href="#st"/><use href="#st" x="21"/><use href="#st" x="42"/><use href="#st" x="63"/><use href="#st" x="84"/></g></svg></div></div>
  <div class="client" style="left:782px"><strong>Lorem ipsum sit</strong><span>Lorem ipsum</span>
    <div class="stars"><svg width="102" height="18" viewBox="0 0 102 18"><g fill="var(--star)"><use href="#st"/><use href="#st" x="21"/><use href="#st" x="42"/><use href="#st" x="63"/><use href="#st" x="84"/></g></svg></div></div>

  <svg class="arrow" style="left:18px" viewBox="0 0 54 54"><circle cx="27" cy="27" r="27" fill="var(--brown)"/><path d="M31 15 19 27l12 12" fill="none" stroke="#fff" stroke-width="3"/></svg>
  <svg class="arrow" style="left:1125px" viewBox="0 0 54 54"><circle cx="27" cy="27" r="27" fill="var(--brown)"/><path d="M23 15l12 12-12 12" fill="none" stroke="#fff" stroke-width="3"/></svg>
</section>

<section class="blog">
  <div class="center" style="top:3058px"><div class="kicker">News &amp; Updates</div><h2 class="title" style="font-size:52px;line-height:60px;margin-top:-4px">Our Blog</h2></div>

  <article class="post" style="left:87px">
    <div class="post-img" role="img" aria-label="Therapist massaging a client's shoulder" style="background:linear-gradient(135deg,#e5d8ca,#6fb5a4 70%,#9ccfc2)"></div>
    <div class="post-box"><div class="date">Friday JAN 25, 2023</div><h4>Post 1 Headline</h4><p>Lorem ipsum dolor sit amet, consectetur adipi</p><a class="read">Read More</a></div>
  </article>
  <article class="post" style="left:438px">
    <div class="post-img" role="img" aria-label="Client receiving a head massage" style="background:linear-gradient(135deg,#7b3a2c,#c0504a 40%,#e2b59c)"></div>
    <div class="post-box"><div class="date">Friday JAN 25, 2023</div><h4>Post 1 Headline</h4><p>Lorem ipsum dolor sit amet, consectetur adipi</p><a class="read">Read More</a></div>
  </article>
  <article class="post" style="left:796px">
    <div class="post-img" role="img" aria-label="Hands giving a back massage" style="background:linear-gradient(135deg,#6d3a2a,#d59a80 55%,#8a4a36)"></div>
    <div class="post-box"><div class="date">Friday JAN 25, 2023</div><h4>Post 1 Headline</h4><p>Lorem ipsum dolor sit amet, consectetur adipi</p><a class="read">Read More</a></div>
  </article>

  <a class="btn-outline">View More</a>
</section>

<footer class="site-footer">
  <div class="footer-brand"><span class="brand-dot"></span>Willowmere Group</div>

  <div class="footer-col" style="left:373px">
    <h5>Quick Links</h5>
    <ul class="quick-links"><li>Home</li><li>About Us</li><li>Services</li><li>Resources</li><li>Blog</li><li>Contact Us</li></ul>
  </div>

  <div class="footer-col" style="left:562px">
    <h5>Contact Us</h5>
    <div class="contact-row" style="margin-top:30px"><svg width="22" height="22" viewBox="0 0 22 22"><rect width="22" height="22" rx="4" fill="#fff"/><path d="M11 4a5 5 0 0 0-5 5c0 4 5 9 5 9s5-5 5-9a5 5 0 0 0-5-5zm0 7a2 2 0 1 1 0-4 2 2 0 0 1 0 4z" fill="var(--brown)"/></svg><span>Address line Dummy Here<br>Address line Here</span></div>
    <div class="contact-row" style="margin-top:24px"><svg width="22" height="22" viewBox="0 0 22 22"><rect width="22" height="22" rx="4" fill="#fff"/><path d="M7 5l3 3-1.5 2a8 8 0 0 0 3.5 3.5L14 12l3 3-2 2C10 17 5 12 5 7z" fill="var(--brown)"/></svg><span>+012 345 6789</span></div>
    <div class="contact-row"><svg width="22" height="22" viewBox="0 0 22 22"><rect width="22" height="22" rx="4" fill="#fff"/><rect x="5" y="7" width="12" height="8" fill="var(--brown)"/><path d="M5 7l6 5 6-5" fill="none" stroke="#fff" stroke-width="1.2"/></svg><span>hello@willowmere.example</span></div>
  </div>

  <div class="footer-col newsletter" style="left:864px">
    <h5>Our Newsletter</h5>
    <p>Subscribe our newsletter to get the latest news.</p>
    <div class="field"></div>
    <div class="subscribe">SUBSCRIBE</div>
  </div>
</footer>

<div class="copyright">Copyright © 2023 All Rights Reserved By The Willowmere Group</div>

</body>
</html>
```